Zielgruppe
Wir eröffnen zum 01.01.2024 ein Ladenlokal 'Nordalis', welches Anwendungen zum Thema Wellness, Gesundheit, Anti Aging anbieten. Wie der Name schon sagt 'NORD' haben wir eine Kältekammer.
Aufgabenstellung
Ich hätte gerne auf dem Flyer die 3 Behandlungen und die Vorteile kurz erklärt:
https://www.velmarix.net/de/produkte/kaeltekammern/frostline-max/
https://tavo-raum.de/puls-ems-anzeige/
http://www.quenter-med.de/download/QUENTER_drainova_D.pdf
Außerdem die Kontaktdaten und die Öffnungszeiten: (erstmal als Platzhalter)
Es sollte ein OPENING Flyer sein - vielleicht eine Opening-Rabatt-Aktion???
Das Logo ist schwarz / weiss, der Laden auch

```html
<!DOCTYPE html>
<html lang="de">
<head>
<meta charset="utf-8">
<title>Nordalis – Große Eröffnung</title>
<link rel="stylesheet" href="https://fonts.googleapis.com/css2?family=Anton&family=Montserrat:wght@300;400;500;600;700;800&display=swap">
<style>
  :root {
    --backdrop: #8e8e8e;
    --paper: #ffffff;
    --ink: #111111;
    --band: #000000;
    --teal: #1fbfd0;
    --teal-dark: #0aa0b2;
    --text-light: #ffffff;
    --skin-1: #f0d9c6;
    --skin-2: #d9b79b;
    --family-1: #d9dcdc;
    --family-2: #8fa3b4;
  }
  * { box-sizing: border-box; margin: 0; padding: 0; }
  html, body { width: 1200px; height: 1117px; overflow: hidden; }
  body { background: var(--backdrop); font-family: "Montserrat", sans-serif; }

  .flyer {
    position: absolute; left: 246px; top: 59px;
    width: 708px; height: 1000px;
    background: var(--paper); overflow: hidden;
  }

  .headline-main {
    position: absolute; left: 40px; top: 26px;
    font-family: "Anton", sans-serif; font-size: 158px; line-height: 1;
    color: #231f20; letter-spacing: -4px;
    transform: scaleY(1.05); transform-origin: top left;
    white-space: nowrap;
  }
  .headline-sub {
    position: absolute; left: 40px; top: 199px;
    font-family: "Anton", sans-serif; font-size: 67px; line-height: 1;
    color: var(--teal); letter-spacing: 14px;
    white-space: nowrap;
  }

  .brand-name {
    position: absolute; left: 505px; top: 22px;
    font-size: 29px; font-weight: 400; letter-spacing: 3px; color: var(--ink);
    white-space: nowrap;
  }

  .info-band {
    position: absolute; left: 0; top: 292px; width: 708px; height: 270px;
    background: linear-gradient(90deg, #12262c 0%, #050a0c 35%, var(--band) 60%);
    color: var(--text-light);
  }
  .band-divider {
    position: absolute; left: 383px; top: 43px; width: 2px; height: 206px; background: var(--teal);
  }
  .treatments { position: absolute; left: 46px; top: 38px; width: 330px; }
  .treatments h2 { font-size: 26px; font-weight: 700; margin-left: 5px; margin-bottom: 12px; }
  .treatment { display: flex; gap: 8px; margin-bottom: 20px; }
  .treatment-num { color: var(--teal); font-weight: 700; font-size: 15px; width: 12px; flex: none; }
  .treatment h3 { font-size: 12.5px; font-weight: 600; line-height: 1.2; }
  .treatment p { font-size: 9.6px; font-weight: 400; line-height: 1.2; }

  .benefits { position: absolute; left: 406px; top: 48px; width: 290px; }
  .benefits h2 { font-size: 26px; font-weight: 700; margin-bottom: 12px; }
  .benefit { display: flex; gap: 9px; margin-bottom: 12px; font-size: 12.5px; line-height: 1.2; }
  .benefit svg { flex: none; margin-top: 2px; }

  .family-photo {
    position: absolute; left: 476px; top: 68px; width: 260px; height: 260px;
    border-radius: 50%; background: var(--paper);
  }
  .family-photo::before {
    content: ""; position: absolute; inset: 0; border-radius: 50%;
    border: 10px solid var(--teal);
  }
  .family-photo-fill {
    position: absolute; inset: 16px; border-radius: 50%;
    background: radial-gradient(circle at 50% 35%, var(--family-1), var(--family-2));
  }

  .portrait-photo {
    position: absolute; left: 0; top: 550px; width: 362px; height: 450px;
    background: radial-gradient(ellipse at 45% 40%, var(--skin-1) 0%, var(--skin-2) 60%, #fff 100%);
  }

  .promo-special {
    position: absolute; left: 338px; top: 578px;
    font-size: 74px; font-weight: 800; color: var(--teal); letter-spacing: -2px; line-height: 1;
  }
  .promo-main {
    position: absolute; left: 364px; top: 640px;
    font-size: 74px; font-weight: 800; color: var(--ink); letter-spacing: -1px; line-height: 1;
  }

  .hours {
    position: absolute; left: 315px; top: 726px; width: 377px; height: 107px;
    background: var(--teal); border-radius: 12px; color: var(--text-light);
  }
  .hours-title {
    position: absolute; left: 15px; top: 0; width: 272px; height: 36px;
    background: var(--teal-dark); border-radius: 0 0 12px 0;
    text-align: center; font-weight: 700; font-size: 17px; line-height: 36px;
  }
  .hours-slot { position: absolute; top: 46px; }
  .hours-slot .day { font-size: 14px; font-weight: 700; line-height: 1; }
  .hours-slot .time { font-family: "Anton", sans-serif; font-size: 34px; line-height: 1.05; }
  .hours-slot.weekday { left: 32px; }
  .hours-slot.weekend { left: 212px; }
  .hours-divider { position: absolute; left: 193px; top: 50px; width: 2px; height: 42px; background: var(--text-light); }

  .contact { position: absolute; left: 375px; top: 846px; }
  .contact-line { display: flex; align-items: center; gap: 14px; font-size: 27px; color: var(--ink); line-height: 31px; }
  .contact-line svg { flex: none; }
  .contact-line.phone { margin-top: 8px; margin-left: -8px; gap: 10px; font-family: "Anton", sans-serif; font-size: 48px; line-height: 52px; }

  .footer-stripe { position: absolute; left: 336px; top: 986px; width: 372px; height: 14px; background: var(--teal); }
</style>
</head>
<body>
<main class="flyer">
  <div class="headline-main">GROSSE</div>
  <div class="headline-sub">ERÖFFNUNG</div>

  <div class="brand-name">NORDALIS</div>

  <section class="info-band">
    <div class="treatments">
      <h2>3 Behandlungen</h2>
      <div class="treatment"><span class="treatment-num">1</span><div><h3>Lorem ipsum dolor sit amet,</h3><p>Lorem ipsum dolor sit amet, consectetur adipiscing elit, sed do eiusmod tempor incididunt ut labore et dolore magna aliqua.</p></div></div>
      <div class="treatment"><span class="treatment-num">2</span><div><h3>Lorem ipsum dolor sit amet,</h3><p>Lorem ipsum dolor sit amet, consectetur adipiscing elit, sed do eiusmod tempor incididunt ut labore et dolore magna aliqua.</p></div></div>
      <div class="treatment"><span class="treatment-num">3</span><div><h3>Lorem ipsum dolor sit amet,</h3><p>Lorem ipsum dolor sit amet, consectetur adipiscing elit, sed do eiusmod tempor incididunt ut labore et dolore magna aliqua.</p></div></div>
    </div>
    <div class="band-divider"></div>
    <div class="benefits">
      <h2>Ihre Vorteile</h2>
      <div class="benefit"><svg width="13" height="13" viewBox="0 0 14 14"><circle cx="7" cy="7" r="5.8" fill="none" stroke="#1fbfd0" stroke-width="1.5"/><path d="M4 7l2.2 2.2L11.5 3.5" fill="none" stroke="#1fbfd0" stroke-width="1.6"/></svg><span>Lorem ipsum dolor sit amet, consectetur adipiscing elit,</span></div>
      <div class="benefit"><svg width="13" height="13" viewBox="0 0 14 14"><circle cx="7" cy="7" r="5.8" fill="none" stroke="#1fbfd0" stroke-width="1.5"/><path d="M4 7l2.2 2.2L11.5 3.5" fill="none" stroke="#1fbfd0" stroke-width="1.6"/></svg><span>Lorem ipsum dolor sit amet, consectetur adipiscing elit,</span></div>
      <div class="benefit"><svg width="13" height="13" viewBox="0 0 14 14"><circle cx="7" cy="7" r="5.8" fill="none" stroke="#1fbfd0" stroke-width="1.5"/><path d="M4 7l2.2 2.2L11.5 3.5" fill="none" stroke="#1fbfd0" stroke-width="1.6"/></svg><span>Lorem ipsum dolor sit amet, consectetur adipiscing elit,</span></div>
      <div class="benefit"><svg width="13" height="13" viewBox="0 0 14 14"><circle cx="7" cy="7" r="5.8" fill="none" stroke="#1fbfd0" stroke-width="1.5"/><path d="M4 7l2.2 2.2L11.5 3.5" fill="none" stroke="#1fbfd0" stroke-width="1.6"/></svg><span>Lorem ipsum dolor sit amet, consectetur adipiscing elit,</span></div>
    </div>
  </section>

  <div class="family-photo"><div class="family-photo-fill" role="img" aria-label="Foto: glückliche Familie spielt zusammen auf dem Sofa"></div></div>

  <div class="portrait-photo" role="img" aria-label="Foto: Porträt einer Frau mit blondem Haar und gepflegter Haut"></div>

  <div class="promo-special">SPECIAL</div>
  <div class="promo-main">PROMO</div>

  <section class="hours">
    <div class="hours-title">Öffnungszeiten:</div>
    <div class="hours-slot weekday"><div class="day">MONDAY - FRIDAY</div><div class="time">9:00 - 6:00</div></div>
    <div class="hours-divider"></div>
    <div class="hours-slot weekend"><div class="day">SATURDAY</div><div class="time">11:00 - 4:00</div></div>
  </section>

  <section class="contact">
    <div class="contact-line"><svg width="22" height="22" viewBox="0 0 24 24" fill="none" stroke="#1fbfd0" stroke-width="1.4"><circle cx="12" cy="12" r="10"/><ellipse cx="12" cy="12" rx="4.5" ry="10"/><path d="M2 12h20M4 7h16M4 17h16"/></svg><span>www.nordalis.com</span></div>
    <div class="contact-line"><svg width="22" height="22" viewBox="0 0 24 24" fill="none" stroke="#1fbfd0" stroke-width="1.4"><rect x="2" y="5" width="20" height="14"/><path d="M2 5l10 8 10-8M2 19l7-7M22 19l-7-7"/></svg><span>info@nordalis.com</span></div>
    <div class="contact-line phone"><svg width="40" height="40" viewBox="0 0 40 40"><circle cx="20" cy="20" r="20" fill="#1fbfd0"/><path d="M14 10c1.5-.6 2.5.2 3.2 2l1.3 3c.4 1 .1 1.8-.8 2.4l-1.3.9c.9 2.4 2.7 4.3 5 5.4l1-1.2c.7-.8 1.5-1 2.4-.5l3 1.5c1.6.8 2.2 1.8 1.5 3.2-1.2 2.5-3.6 3.4-6.5 2.2-5-2-8.6-5.800-10.5-10.8-1-2.8-.3-5.2 1.7-8.1z" fill="#fff"/></svg><span>123-456-7890</span></div>
  </section>

  <div class="footer-stripe"></div>
</main>
</body>
</html>
```